Radiant Crossing - An Exciting Mission & Book Cover Project

Help me to inspire people to live their best life! This is a mission, not just a design project.
I need a Book Cover designed to keep me inspired on the process of writing my book.
Book Title: Radiant Crossing
Tag Line: Three Simple Steps to get out of your own way, SuperCharge your Life and Step into Purpose!
Author: Marlis Quenby

The three steps are: Ownership, Vision and Action (Not sure if this should be on the front or back of the book cover)

The book is a self-help, motivational book. Personal development.
The cover needs to be strong and capture peoples attention, especially with competing shelf space. I almost see a fire ball of flame or explosion that will grab peoples attention.
My company is The Lantern Institute. I have added the company logo and a few pages of my presentation and topic outline to give an idea.
Maybe: The Lantern Institute logo on back of the cover. website is marlisquenby.com

THOUGHT: People should be able to take a photo of them holding the book cover showing what area of life they want Radiant Crossing in. This is why the front cover must be so visual and powerful that they want to take a photo with it. Ie. Explosion, fire, strong and bold.

Target Market(s)

Anyone who feels stuck and needs to breakthrough and move forward in life.

Industry/Entity Type

Motivation

Font styles to use
Serif
Sans Serif

Colors
ec1f27
f37122
fbed22

Requirements
Must have
• The design must be STRONG, SIMPLE, STAND OUT ON BOOK SHELVES.
Must have an open file to swap the photo and copy out.

Back Cover Page
1) Summary
2) 2-3 testimonials. One sentence.
3) About the Author (maybe with photo)
4) Lantern Institute logo
5) Website: radiantcrossing.com and marlisquenby.com
Nice to have
• If my photo works somewhere that would be great. I will change the photo later.
Added Where's Your Harbor? a nice cover example.
Should not have
• Right now I am writing the summary for the back of the cover. For now use Loreum Ipsum text and 2-3 recommendations. Again, I will get these only later.

```html
<!DOCTYPE html>
<html lang="en">
<head>
<meta charset="utf-8">
<title>Radiant Crossing – Book Cover</title>
<link rel="stylesheet" href="https://fonts.googleapis.com/css2?family=Montserrat:wght@300;400;800;900&family=Roboto:wght@400&family=Tinos&display=swap">
<style>
  :root {
    --canvas: #e4e4e6;
    --spine: #1a1e38;
    --title-yellow: #f2ec2e;
    --text-white: #ffffff;
    --frame-line: #c9cde0;
    --front-deep: #1b1a2e;
    --front-glow: #ffd27a;
    --front-fire: #e0671f;
    --back-deep: #0c1230;
    --back-blue: #1f4fa8;
    --back-light: #7fc4ee;
  }
  * { margin: 0; padding: 0; box-sizing: border-box; }
  html, body { width: 1200px; height: 1000px; overflow: hidden; background: var(--canvas); }
  .spread { position: relative; width: 1200px; height: 1000px; }

  .panel { position: absolute; top: 96px; height: 808px; overflow: hidden; }
  .front { left: 16px; width: 538px; }
  .spine { left: 554px; width: 91px; background: var(--spine); }
  .back { left: 645px; width: 539px; }

  .cover-photo { position: absolute; inset: 0; }
  .front .cover-photo {
    background:
      radial-gradient(ellipse 34% 28% at 50% 74%, var(--front-glow) 0%, rgba(243,113,34,0.85) 40%, rgba(243,113,34,0) 100%),
      radial-gradient(ellipse 70% 40% at 50% 80%, rgba(224,103,31,0.9) 0%, rgba(120,50,30,0.6) 55%, rgba(27,26,46,0) 100%),
      linear-gradient(180deg, var(--front-deep) 0%, #2b1f2e 45%, #6a3a24 75%, #a4582a 100%);
  }
  .back .cover-photo {
    background:
      radial-gradient(ellipse 30% 22% at 18% 8%, rgba(240,220,170,0.8) 0%, rgba(240,220,170,0) 100%),
      radial-gradient(ellipse 45% 55% at 75% 48%, var(--back-light) 0%, rgba(31,79,168,0.7) 40%, rgba(12,18,48,0) 100%),
      linear-gradient(160deg, var(--back-deep) 0%, var(--back-blue) 55%, var(--back-deep) 100%);
  }

  .title {
    position: absolute; left: 0; right: 0; text-align: center;
    font-family: "Montserrat", sans-serif; font-weight: 900;
    color: var(--title-yellow); line-height: 1;
  }
  .title .line-1 { display: block; font-size: 74px; letter-spacing: 1px; }
  .title .line-2 { display: block; font-size: 46px; margin-top: 10px; letter-spacing: 1px; }
  .front .title { top: 36px; }
  .back .title { top: 30px; }

  .tagline {
    position: absolute; top: 244px; left: 30px; right: 30px; text-align: center;
    font-family: "Montserrat", sans-serif; font-weight: 400; font-size: 21px;
    line-height: 26px; color: var(--text-white);
  }
  .front-author {
    position: absolute; top: 736px; left: 0; right: 0; text-align: center;
    font-family: "Montserrat", sans-serif; font-weight: 800; font-size: 33px;
    color: var(--title-yellow);
  }

  .spine-text {
    position: absolute; left: 50%; transform: translateX(-50%);
    writing-mode: vertical-rl;
    font-family: "Montserrat", sans-serif; font-weight: 800; font-size: 25px;
    color: var(--title-yellow); letter-spacing: 1px; white-space: nowrap;
  }
  .spine-title { top: 34px; }
  .spine-author { top: 546px; }

  .summary {
    position: absolute; left: 50px; right: 40px; text-align: center;
    font-family: "Tinos", serif; font-size: 18.5px; line-height: 26px;
    text-transform: uppercase; color: var(--text-white);
  }
  .summary-one { top: 204px; }
  .summary-two { top: 306px; }

  .author-photo-frame {
    position: absolute; left: 41px; top: 480px; width: 134px; height: 116px;
    border: 1.5px solid var(--frame-line); background: rgba(12,18,48,0.55);
  }
  .author-name {
    position: absolute; left: 192px; top: 488px;
    font-family: "Roboto", sans-serif; font-size: 28px; color: var(--title-yellow);
  }
  .author-bio {
    position: absolute; left: 192px; top: 540px; width: 310px;
    font-family: "Roboto", sans-serif; font-size: 19px; line-height: 26px; color: var(--text-white);
  }

  .publisher {
    position: absolute; left: 40px; top: 742px; width: 170px;
    display: flex; align-items: center; gap: 6px;
    font-family: "Montserrat", sans-serif; font-weight: 800; font-size: 12.5px;
    color: var(--text-white); text-transform: uppercase;
  }
  .publisher-dot { width: 10px; height: 10px; border-radius: 50%; background: var(--text-white); flex: none; }
</style>
</head>
<body>
<main class="spread">

  <section class="panel front">
    <div class="cover-photo" role="img" aria-label="Fiery explosion rising from the horizon of a planet against a starry sky"></div>
    <h1 class="title"><span class="line-1">RADIANT</span><span class="line-2">CROSSING</span></h1>
    <p class="tagline">“ Three Simple Steps to get out of your<br>own way, SuperCharge<br>your Lifeand Step into Purpose ”</p>
    <p class="front-author">MARLIS QUENBY</p>
  </section>

  <section class="panel spine">
    <span class="spine-text spine-title">RADIANT CROSSING</span>
    <span class="spine-text spine-author">MARLIS QUENBY</span>
  </section>

  <section class="panel back">
    <div class="cover-photo" role="img" aria-label="Blurred deep space scene with a glowing blue nebula and planets"></div>
    <h2 class="title"><span class="line-1">RADIANT</span><span class="line-2">CROSSING</span></h2>
    <p class="summary summary-one">Lorem Ipsum is simply dummy text of<br>the printing and typesetting<br>industry. Lorem Ipsum has been the</p>
    <p class="summary summary-two">Lorem Ipsum is simply dummy text of<br>the printing and typesetting<br>industry. Lorem Ipsum has been the<br>industry's standard dummy</p>
    <div class="author-photo-frame"></div>
    <p class="author-name">MARLIS QUENBY</p>
    <p class="author-bio">Lorem Ipsum is simply<br>dummy text of the printing and</p>
    <div class="publisher"><span class="publisher-dot"></span><span>The Lantern Institute</span></div>
  </section>

</main>
</body>
</html>
```